依頼詳細
資料請求に特化したいので、よくある縦に長いランディングページではなく、ぱっと見てとりあえず資料を請求したくなるようなページが希望です。
したがって、キャッチコピー(アイキャッチ)はファーストビュー(画面に見える形)で、縦は長くてもA4判の縦の比率でお願いします。
必ず入れてほしい項目は「補足説明」に記載の通りですが、その他のキャッチや文章などはお任せです。
資料請求したくなるような文面とデザインをご提案いただけましたら幸いです。
サイトURL
http://www.rovino.net/
ページ数
1ページ
希望イメージ
シンプル 複雑
単色 カラフル
暗い 明るい
日常 高級
遊び心 厳粛
未来的 伝統的
女性的 男性的
希望する色
色の指定はありませんが、明るい感じの色でお願いします。くすんだ色・ぼやけた色は好みではありません。
納品ファイル
• 高解像度JPG (.jpg)
• イラストレーター形式 (.ai)
補足説明
必ず入れてほしい項目は以下の通りです。

・サイト名(ひまわりルーム案内所)
※ロゴはそのまま使ってもかまいませんが、ロゴを使わずに色も形も変えてもかまいません。
ランディングページにあったロゴ(フォント)がベストです。(現在のロゴの色や形にこだわっていません)
・参加企業のパンフレット表紙
※実際に送るパンフがわかった方が、コンバージョンがよくなると思いますので..。
※参加企業は現在7社ですので、パンフも7点となります。ただし、今後は増減する可能性もありますので、7点に固執したデザインではなく、6点や8点になっても弊社で変更できるデザインを希望します。
・参加企業一覧とチェックボックス
※ランディングページ=資料請求ページになり、すぐに資料請求ができるようにします。
※現在の資料請求ページは以下の通りです。
http://www.rovino.net/rv/10.html
・トップページに戻るボタン
※ランディングページが孤立しないように、本来のサイトのトップに戻るボタンかテキストを入れてください。

なお、各社のパンフレットとリスティング広告に使用するバナーの見本は以下からDLしてご確認ください。
http://www.kz4.co.jp/pb.zip
納品ファイルに、イラストレーター形式 (.ai)を指定しましたが、イラストレーターがない場合は、jpgのみでもかまいません。
ただし、ご提案時に記載をしてください。
「イラストレーターがない場合は、jpgのみでもかまいません。」と追記しましたが、hmtl作成時にテキストが必要ですので、イラストレーターに替わるソフトがありましたら、記載していただけますよう、お願いいたします。(フォトショップやファイアーワークスなどです)
依頼途中で、サイトの参加会社が変わってしまったので、パンフレットを差し替えてアップしました。
同じURLですが、パンフを差し替えていますので、ご確認ください。
※既にダウンロード済みで、ご提案を製作中の場合は、古いパンフでも問題ありません。
(レイアウト確認だけですので..)
ただし、採用された場合は、最新のパンフレットで納品をお願いいたします。

インパクトには掛けますが、全体的な構成が整っていましたので、選ばせていただきました。

たくさんのご提案をいただき、ありがとうございました。
修正していただいた方はお手数をお掛けして、申し訳ございませんでした。
機会がございましたら、またよろしくお願いいたします。

```html
<!DOCTYPE html>
<html lang="ja">
<head>
<meta charset="utf-8">
<title>ひまわりルーム案内所 一括資料請求</title>
<link href="https://fonts.googleapis.com/css2?family=Noto+Sans+JP:wght@400;700;900&display=swap" rel="stylesheet">
<style>
:root{
  --bg:#fde9a6;
  --panel:#ffffff;
  --orange:#f08a1c;
  --orange-dark:#e0620e;
  --red:#e8401c;
  --green:#6ab42d;
  --peach:#fff3df;
  --line:#f3c489;
  --text:#4a3a2a;
  --muted:#8a7a6a;
}
*{box-sizing:border-box;margin:0;padding:0}
html,body{width:794px;height:1200px;overflow:hidden}
body{background:var(--bg);font-family:"Noto Sans JP",sans-serif;color:var(--text);position:relative}
.page{position:absolute;left:80px;top:0;width:634px;height:1200px;background:var(--panel);box-shadow:0 0 10px rgba(200,140,40,.25)}
.site-header{height:46px;display:flex;align-items:center;padding-left:16px}
.site-name{font-size:20px;font-weight:900;color:var(--orange)}
.hero{position:relative;height:244px}
.hero-photo{position:absolute;inset:0;background:linear-gradient(135deg,#f7eee4,#e9e2da 60%,#d9d1c8)}
.hero-copy{position:absolute;left:16px;top:132px;width:600px}
.badges{display:flex;gap:6px;position:absolute;left:0;top:22px}
.badge{background:var(--orange);color:#fff;font-weight:900;font-size:26px;padding:4px 10px;border-radius:4px}
.hero-title{position:absolute;right:10px;top:0;text-align:right;font-weight:900;color:var(--red);line-height:1.15}
.hero-title .l1{font-size:26px;display:block}
.hero-title .l2{font-size:46px;display:block;color:#d2321a}
.section-title{text-align:center;color:var(--orange-dark);font-weight:700;font-size:17px;margin:30px 0 8px}
.brochures{margin:0 22px;background:var(--peach);border:2px solid var(--line);border-radius:6px;padding:12px 14px 8px;height:422px;position:relative}
.brochure-row{display:grid;grid-template-columns:repeat(5,1fr);gap:12px;margin-bottom:10px}
.brochure{display:flex;flex-direction:column;align-items:center}
.tab{width:100%;background:var(--orange);color:#fff;font-size:9px;text-align:center;padding:3px 0;border-radius:3px 3px 0 0;white-space:nowrap;overflow:hidden}
.tab.green{background:var(--green)}
.cover{width:100%;height:148px}
.caption{font-size:9px;color:var(--muted);margin-top:3px;white-space:nowrap}
.guide-photo{position:absolute;right:14px;bottom:10px;width:190px;height:196px;background:linear-gradient(180deg,#fbe7e2,#f3d4c6)}
.guide-note{position:absolute;right:150px;bottom:150px;background:#fff;border:2px solid var(--orange);border-radius:50%;width:66px;height:50px;font-size:10px;font-weight:700;color:var(--orange-dark);display:flex;align-items:center;justify-content:center;text-align:center;line-height:1.2}
.cta-banner{position:relative;margin:22px 40px 0;background:var(--orange);color:#fff;font-weight:700;font-size:16px;text-align:center;padding:11px 0;border-radius:4px}
.cta-banner svg{position:absolute;left:50%;bottom:-16px;transform:translateX(-50%)}
.company-table{margin:26px 22px 0;width:590px;border-collapse:collapse;font-size:11px}
.company-table th{background:var(--orange);color:#fff;font-weight:700;height:24px}
.company-table td{border-bottom:1px solid var(--line);height:22px;padding:0 6px}
.company-table tr:nth-child(even) td{background:#fffaf2}
.check{width:12px;height:12px;border:1px solid #999;display:inline-block;vertical-align:middle;margin-right:6px;background:#fff}
.area{color:var(--muted);font-size:10px}
.detail-btn{display:inline-block;background:var(--orange);color:#fff;font-size:10px;padding:2px 10px;border-radius:3px}
.submit{display:block;margin:24px auto 0;width:270px;height:44px;border-radius:22px;background:linear-gradient(180deg,#f9a640,var(--orange-dark));color:#fff;font-weight:900;font-size:20px;text-align:center;line-height:44px;letter-spacing:2px}
.back-top{position:absolute;right:16px;bottom:12px;font-size:11px;color:var(--muted)}
</style>
</head>
<body>
<div class="page">
  <header class="site-header"><span class="site-name">ひまわりルーム案内所</span></header>

  <section class="hero">
    <div class="hero-photo" role="img" aria-label="笑顔の女子学生二人の写真"></div>
    <div class="hero-copy">
      <div class="badges"><span class="badge">簡単</span><span class="badge">無料</span></div>
      <h1 class="hero-title"><span class="l1">ひまわりルーム案内所の</span><span class="l2">一括資料請求</span></h1>
    </div>
  </section>

  <h2 class="section-title">資料請求可能な学生マンション運営会社様</h2>
  <section class="brochures">
    <div class="brochure-row">
      <div class="brochure"><div class="tab">全国17都道府県</div><div class="cover" role="img" aria-label="パンフレット表紙" style="background:linear-gradient(#f5f09a,#b8dc7a)"></div><div class="caption">キャンパスネスト</div></div>
      <div class="brochure"><div class="tab">東北・関東・関西</div><div class="cover" role="img" aria-label="パンフレット表紙" style="background:linear-gradient(#8fd0ea,#f4c6d8)"></div><div class="caption">学生住まいセンター</div></div>
      <div class="brochure"><div class="tab">東京・千葉・埼玉</div><div class="cover" role="img" aria-label="パンフレット表紙" style="background:linear-gradient(#f2b6c8,#f9e4ea)"></div><div class="caption">学生寮総合ガイド</div></div>
      <div class="brochure"><div class="tab">東京・千葉・埼玉</div><div class="cover" role="img" aria-label="パンフレット表紙" style="background:linear-gradient(#9ad6e8,#e8f4f8)"></div><div class="caption">スチューデントホーム</div></div>
      <div class="brochure"><div class="tab">東京・神奈川</div><div class="cover" role="img" aria-label="パンフレット表紙" style="background:linear-gradient(#c9e7f2,#6fb8d8)"></div><div class="caption">学生ライフ案内</div></div>
    </div>
    <div class="brochure-row">
      <div class="brochure"><div class="tab green">大阪・京都</div><div class="cover" role="img" aria-label="パンフレット表紙" style="background:linear-gradient(#c6e6a4,#f5f7d8)"></div><div class="caption">みどり商産</div></div>
      <div class="brochure"><div class="tab">京都</div><div class="cover" role="img" aria-label="パンフレット表紙" style="background:linear-gradient(#f6c44a,#e8772a)"></div><div class="caption">まなびルーム</div></div>
      <div class="brochure"><div class="tab">首都圏</div><div class="cover" role="img" aria-label="パンフレット表紙" style="background:linear-gradient(#f7b6d2,#fbe2ee)"></div><div class="caption">へやさがしっ!</div></div>
    </div>
    <div class="guide-photo" role="img" aria-label="パンフレットを指し示す女性の写真"></div>
    <div class="guide-note">気になる<br>資料を<br>チェック!</div>
  </section>

  <div class="cta-banner">気になる運営会社にチェックを入れて、資料請求しましょう!
    <svg width="40" height="18" viewBox="0 0 40 18"><polygon points="0,0 40,0 20,18" fill="#f08a1c"/></svg>
  </div>

  <table class="company-table">
    <thead><tr><th style="width:44%">会社名</th><th style="width:38%">営業地域</th><th>詳細</th></tr></thead>
    <tbody>
      <tr><td><span class="check"></span>キャンパスネスト</td><td class="area">全国(首都圏含む)</td><td><span class="detail-btn">詳しくはこちら</span></td></tr>
      <tr><td><span class="check"></span>学生住まいセンター</td><td class="area">東北・北関東・京都・大阪</td><td><span class="detail-btn">詳しくはこちら</span></td></tr>
      <tr><td><span class="check"></span>学生寮総合ガイドセンター</td><td class="area">東京・千葉・埼玉・神奈川</td><td><span class="detail-btn">詳しくはこちら</span></td></tr>
      <tr><td><span class="check"></span>東京/湘南スチューデントホーム</td><td class="area">東京・千葉・埼玉・神奈川</td><td><span class="detail-btn">詳しくはこちら</span></td></tr>
      <tr><td><span class="check"></span>みどり商産</td><td class="area">大阪・京都</td><td><span class="detail-btn">詳しくはこちら</span></td></tr>
      <tr><td><span class="check"></span>ハルノ住建/まなびルーム</td><td class="area">京都</td><td><span class="detail-btn">詳しくはこちら</span></td></tr>
      <tr><td><span class="check"></span>へやさがしっ!</td><td class="area">東京・千葉・埼玉・神奈川</td><td><span class="detail-btn">詳しくはこちら</span></td></tr>
    </tbody>
  </table>

  <a class="submit">資料を請求する</a>
  <a class="back-top">ひまわりルーム案内所トップへ戻る</a>
</div>
</body>
</html>
```